Business Card for Veltrano, a french tech company

Tech company
New technologies
Serious design
Dark theme

User info :
Name: Mathis CORLAVE
Position: Co-Founder & CEO
Tel: (+33) 6 58 24 90 37
Email: mathis@veltrano.io
Website: www.veltrano.io
Address: 17 rue des Tanneurs 69002 LYON

Attached is the business logo file.

```html
<!DOCTYPE html>
<html lang="en">
<head>
<meta charset="utf-8">
<title>Veltrano – Business Card</title>
<link rel="stylesheet" href="https://fonts.googleapis.com/css2?family=Montserrat:wght@700;800&family=Open+Sans:wght@400;600&display=swap">
<style>
  :root {
    --backdrop: #1c1c1f;
    --navy-deep: #15195e;
    --navy: #232a86;
    --pattern-blue: #3a55b8;
    --magenta: #e0218a;
    --purple: #9b3aa8;
    --ink-navy: #1f2a5c;
    --ink: #1b1b24;
    --paper: #ffffff;
    --blush: #f6e4ef;
  }
  * { box-sizing: border-box; margin: 0; padding: 0; }
  html, body { width: 1200px; height: 780px; overflow: hidden; }
  body {
    background: var(--backdrop);
    font-family: "Open Sans", Arial, sans-serif;
    display: flex;
    align-items: center;
    justify-content: center;
    gap: 44px;
  }
  .card {
    position: relative;
    width: 520px;
    height: 320px;
    border-radius: 22px;
    overflow: hidden;
  }

  /* Front */
  .card-front {
    background: var(--navy-deep);
    border-bottom: 4px solid var(--magenta);
    border-left: 3px solid var(--magenta);
  }
  .front-pattern {
    position: absolute;
    inset: 0;
    background:
      radial-gradient(ellipse at 70% 20%, rgba(58,85,184,0.35), transparent 60%),
      linear-gradient(135deg, var(--navy) 0%, var(--navy-deep) 100%);
  }
  .front-wordmark {
    position: absolute;
    inset: 0;
    display: flex;
    align-items: center;
    justify-content: center;
    font-family: "Montserrat", Arial, sans-serif;
    font-weight: 800;
    font-size: 58px;
    letter-spacing: 1px;
    color: var(--paper);
  }

  /* Back */
  .card-back {
    background: var(--paper);
    border-bottom: 4px solid var(--magenta);
    border-left: 3px solid var(--magenta);
  }
  .holder {
    position: absolute;
    top: 44px;
    right: 0;
    text-align: right;
  }
  .holder-name {
    display: inline-flex;
    align-items: stretch;
    font-family: "Montserrat", Arial, sans-serif;
    font-weight: 700;
    font-size: 24px;
    line-height: 1;
  }
  .holder-name .name-text {
    background: linear-gradient(90deg, var(--blush), rgba(246,228,239,0.2));
    padding: 6px 12px 6px 14px;
  }
  .first-name { color: var(--purple); }
  .last-name { color: var(--ink-navy); }
  .holder-name .name-tab {
    width: 12px;
    background: var(--magenta);
  }
  .holder-role {
    margin-top: 6px;
    margin-right: 30px;
    font-size: 14px;
    font-weight: 600;
    color: var(--ink);
  }
  .back-wordmark {
    position: absolute;
    left: 32px;
    top: 128px;
    font-family: "Montserrat", Arial, sans-serif;
    font-weight: 800;
    font-size: 46px;
    color: var(--purple);
    letter-spacing: 0.5px;
  }
  .address {
    position: absolute;
    left: 34px;
    top: 196px;
    font-size: 13.5px;
    line-height: 1.4;
    color: var(--ink);
  }
  .contacts {
    position: absolute;
    left: 34px;
    top: 244px;
    list-style: none;
    font-size: 13.5px;
    line-height: 1.4;
    color: var(--ink);
  }
  .contacts li { display: flex; align-items: center; gap: 8px; }
  .contacts svg { width: 12px; height: 12px; flex: none; }
</style>
</head>
<body>

  <section class="card card-front" aria-label="Card front">
    <div class="front-pattern" role="img" aria-label="Repeating small brand symbol pattern in blue on navy"></div>
    <div class="front-wordmark">VELTRANO</div>
  </section>

  <section class="card card-back" aria-label="Card back">
    <div class="holder">
      <div class="holder-name">
        <span class="name-text"><span class="first-name">Mathis</span> <span class="last-name">CORLAVE</span></span>
        <span class="name-tab"></span>
      </div>
      <p class="holder-role">Co-Founder &amp; CEO</p>
    </div>

    <div class="back-wordmark">VELTRANO</div>

    <address class="address">17 rue des Tanneurs<br>69002 LYON</address>

    <ul class="contacts">
      <li>
        <svg viewBox="0 0 12 12" aria-hidden="true"><circle cx="6" cy="6" r="6" fill="#9b3aa8"/><path d="M4 3.2l1 1.2-.6.8c.4.8 1 1.4 1.8 1.8l.8-.6 1.2 1-.6 1.2C5.6 8.4 3.6 6.4 3.4 3.8z" fill="#fff"/></svg>
        (+33) 6 58 24 90 37
      </li>
      <li>
        <svg viewBox="0 0 12 12" aria-hidden="true"><circle cx="6" cy="6" r="6" fill="#9b3aa8"/><circle cx="6" cy="6" r="3.2" fill="none" stroke="#fff" stroke-width="0.9"/><path d="M2.8 6h6.4M6 2.8c-1.4 1.8-1.4 4.6 0 6.4M6 2.8c1.4 1.8 1.4 4.6 0 6.4" fill="none" stroke="#fff" stroke-width="0.7"/></svg>
        www.veltrano.io
      </li>
      <li>
        <svg viewBox="0 0 12 12" aria-hidden="true"><circle cx="6" cy="6" r="6" fill="#9b3aa8"/><rect x="3" y="4" width="6" height="4.2" rx="0.6" fill="#fff"/><path d="M3.2 4.3L6 6.4l2.8-2.1" fill="none" stroke="#9b3aa8" stroke-width="0.7"/></svg>
        mathis@veltrano.io
      </li>
    </ul>
  </section>

</body>
</html>
```